Buff & Gleam

polished concrete and epoxy coatings flooring company

Target Market(s)

Industrial commercial

Industry/Entity Type

Industrial flooring contractor

Contact Information for Business Card

POLISHED CONCRETE • EPOXY COATING • TERRAZZO RESTORATION • SHOT BLASTING • SURFACE PREPARATION • JOINT FILLING • TILE/ CARPET /GLUE REMOVAL

Colors
0054AA
0677BA
7BADD7
CADEEF
E8F1F8

Requirements
Must have
• email buffandgleamfloors@mailbrook.example Address 47215 Tallowmere Rd, Fraser, MI 48093. Name Ray Tulvin. Services Polished concrete- Epoxy Coatings- Terrazzo restoration-surface preparation- safety striping- joint filling- tile/ carpet/ glue removal phone number 586-700-3926 email buffandgleamfloors.example
Nice to have
• Instagram Facebook logo maybe smaller in the corner

```html
<!DOCTYPE html>
<html lang="en">
<head>
<meta charset="utf-8">
<title>Buff &amp; Gleam — Business Card</title>
<link rel="stylesheet" href="https://fonts.googleapis.com/css2?family=Montserrat:wght@500;600;700;800&display=swap">
<style>
  :root {
    --page-bg: #ffffff;
    --card-black: #000000;
    --card-edge: #0054AA;
    --text-light: #ffffff;
    --blue-deep: #0054AA;
    --blue-mid: #0677BA;
    --blue-soft: #7BADD7;
    --blue-pale: #CADEEF;
    --blue-mist: #E8F1F8;
    --sheen-dark: #050a12;
  }
  * { margin: 0; padding: 0; box-sizing: border-box; }
  html, body {
    width: 1200px; height: 1200px; overflow: hidden;
    background: var(--page-bg);
    font-family: "Montserrat", Arial, sans-serif;
  }
  .stage { position: relative; width: 1200px; height: 1200px; }
  .card {
    position: absolute; top: 316px;
    width: 322px; height: 568px;
    background: var(--card-black);
    border: 1px solid var(--card-edge);
    overflow: hidden;
    color: var(--text-light);
  }
  .card--front { left: 244px; }
  .card--back  { left: 634px; }
  .card__art { position: absolute; inset: 0; width: 100%; height: 100%; }
  .card--back .card__art { transform: scaleX(-1); }

  .brand-name { font-weight: 800; letter-spacing: 0.2px; white-space: nowrap; }
  .brand-tagline { font-weight: 600; white-space: nowrap; color: var(--blue-pale); }

  .front-brand {
    position: absolute; left: 0; right: 0; top: 238px;
    text-align: center; padding-left: 40px;
  }
  .front-brand .brand-name { font-size: 25px; line-height: 1; }
  .front-brand .brand-tagline { font-size: 7.4px; margin-top: 5px; }

  .services {
    position: absolute; left: 26px; top: 327px;
    list-style: none;
    font-weight: 600; font-size: 15px; line-height: 22.6px;
    letter-spacing: 0.2px; white-space: nowrap;
  }
  .services li::before { content: "• "; color: var(--blue-soft); }

  .address {
    position: absolute; left: 0; right: 0; top: 516px;
    text-align: center; font-weight: 500; font-size: 11.6px; letter-spacing: 0.2px;
  }

  .back-brand {
    position: absolute; left: 226px; top: 296px;
    transform: translate(-50%, -50%) rotate(-90deg);
    text-align: left;
  }
  .back-brand .brand-name { font-size: 44px; line-height: 1; }
  .back-brand .brand-tagline { font-size: 11.5px; margin-top: 6px; }

  .contact {
    position: absolute; left: 22px; right: 18px; top: 474px;
    font-size: 11px; line-height: 16px; font-weight: 500;
    text-align: right; white-space: nowrap;
  }
  .contact__name { font-weight: 700; font-size: 13px; color: var(--text-light); }
  .contact__line { color: var(--blue-mist); }
</style>
</head>
<body>
<main class="stage">

  <section class="card card--front" aria-label="Business card front">
    <svg class="card__art" viewBox="0 0 476 839" preserveAspectRatio="none" aria-hidden="true">
      <defs>
        <linearGradient id="sheenLeft" x1="0" y1="0" x2="1" y2="0">
          <stop offset="0" stop-color="#050a12"/>
          <stop offset="0.7" stop-color="#0054AA"/>
          <stop offset="1" stop-color="#003a78"/>
        </linearGradient>
        <linearGradient id="sheenRight" x1="0" y1="0" x2="1" y2="0">
          <stop offset="0" stop-color="#02060c"/>
          <stop offset="0.5" stop-color="#0054AA"/>
          <stop offset="1" stop-color="#7BADD7"/>
        </linearGradient>
      </defs>
      <rect width="476" height="839" fill="url(#sheenLeft)"/>
      <path d="M165 125 Q300 12 476 0 L476 839 L165 839 Z" fill="url(#sheenRight)"/>
      <path d="M0 839 L0 318 Q70 190 165 125 Q390 330 476 745 L476 839 Z" fill="var(--card-black)"/>
    </svg>

    <div class="front-brand">
      <p class="brand-name">Buff &amp; Gleam</p>
      <p class="brand-tagline">polished concrete • epoxy coatings flooring</p>
    </div>

    <ul class="services">
      <li>POLISHED CONCRETE</li>
      <li>EPOXY COATING</li>
      <li>TERRAZZO RESTORATION</li>
      <li>SHOT BLASTING</li>
      <li>SURFACE PREPARATION</li>
      <li>JOINT FILLING</li>
      <li>TILE/ CARPET /GLUE REMOVAL</li>
    </ul>

    <p class="address">47215 Tallowmere Rd, Fraser, MI 48093</p>
  </section>

  <section class="card card--back" aria-label="Business card back">
    <svg class="card__art" viewBox="0 0 476 839" preserveAspectRatio="none" aria-hidden="true">
      <defs>
        <linearGradient id="sheenLeftB" x1="0" y1="0" x2="1" y2="0">
          <stop offset="0" stop-color="#050a12"/>
          <stop offset="0.7" stop-color="#0054AA"/>
          <stop offset="1" stop-color="#003a78"/>
        </linearGradient>
        <linearGradient id="sheenRightB" x1="0" y1="0" x2="1" y2="0">
          <stop offset="0" stop-color="#02060c"/>
          <stop offset="0.5" stop-color="#0054AA"/>
          <stop offset="1" stop-color="#7BADD7"/>
        </linearGradient>
      </defs>
      <rect width="476" height="839" fill="url(#sheenLeftB)"/>
      <path d="M165 125 Q300 12 476 0 L476 839 L165 839 Z" fill="url(#sheenRightB)"/>
      <path d="M0 839 L0 318 Q70 190 165 125 Q390 330 476 730 L476 839 Z" fill="var(--card-black)"/>
    </svg>

    <div class="back-brand">
      <p class="brand-name">Buff &amp; Gleam</p>
      <p class="brand-tagline">polished concrete • epoxy coatings flooring</p>
    </div>

    <div class="contact">
      <p class="contact__name">Ray Tulvin</p>
      <p class="contact__line">586-700-3926</p>
      <p class="contact__line">buffandgleamfloors@mailbrook.example</p>
      <p class="contact__line">buffandgleamfloors.example</p>
    </div>
  </section>

</main>
</body>
</html>
```